Young and modern Electrical company working in the commercial arena.

Wanting a business card design thats modern and will last. Maybe Minimalist? Happy to look at changing my logo

Target Market(s)

Builders, Project Managers

Industry/Entity Type

Electrical

Contact Information for Business Card

Name
Address
Phone number
Job title

Logo Text

our name or just the logo i'm open to ideas

Font styles to use
Sans Serif

Requirements
Nice to have
• would like to keep the purple in our current logo. it's kinda unique to our market
Should not have
• Don't want it to be to busy. simple is best i think

```html
<!DOCTYPE html>
<html lang="en">
<head>
<meta charset="utf-8">
<title>Halvorsen Electrical – Business Card</title>
<link href="https://fonts.googleapis.com/css2?family=Cinzel:wght@600&family=Lato:wght@400;700&display=swap" rel="stylesheet">
<style>
  :root {
    --bg: #4a4a4a;
    --card-dark: #3a3a3a;
    --card-light: #ffffff;
    --brand-purple: #6a00c8;
    --text-light: #f2f2f2;
    --text-dark: #383838;
  }
  html, body {
    margin: 0;
    padding: 0;
    width: 1200px;
    height: 802px;
    overflow: hidden;
    background: var(--bg);
  }
  .canvas {
    position: relative;
    width: 1200px;
    height: 802px;
  }
  .card {
    position: absolute;
    top: 274px;
    width: 442px;
    height: 264px;
    overflow: hidden;
  }
  .card--front {
    left: 136px;
    background: var(--card-dark);
    color: var(--text-light);
    font-family: "Lato", sans-serif;
  }
  .card--back {
    left: 624px;
    background: var(--card-light);
  }
  .accent-panel {
    position: absolute;
    inset: 0;
  }
  .wordmark {
    position: absolute;
    margin: 0;
    font-family: "Lato", sans-serif;
    font-weight: 400;
    text-transform: uppercase;
    line-height: 1;
  }
  .card--front .wordmark {
    left: 26px;
    top: 58px;
    color: var(--text-light);
    font-size: 19px;
    letter-spacing: 2px;
  }
  .card--front .wordmark span { display: block; }
  .card--front .wordmark span + span { margin-top: 5px; font-size: 21px; letter-spacing: 1px; }
  .card--back .wordmark {
    left: 0;
    right: 0;
    top: 100px;
    text-align: center;
    color: var(--text-dark);
    font-size: 27px;
    letter-spacing: 7px;
  }
  .card--back .wordmark span { display: block; }
  .card--back .wordmark span + span { margin-top: 6px; font-size: 31px; letter-spacing: 2px; }
  .person {
    position: absolute;
    left: 24px;
    top: 128px;
  }
  .person__name {
    margin: 0;
    font-family: "Cinzel", serif;
    font-weight: 600;
    font-size: 15px;
    line-height: 17px;
  }
  .person__role {
    margin: 0;
    font-size: 12.5px;
    line-height: 15px;
  }
  .contact {
    position: absolute;
    left: 24px;
    top: 170px;
    margin: 0;
    padding: 0;
    list-style: none;
    font-size: 12.5px;
    line-height: 16px;
  }
  .contact li { display: flex; align-items: center; gap: 4px; }
  .contact svg { width: 10px; height: 10px; fill: var(--text-light); }
  .address {
    position: absolute;
    left: 24px;
    top: 208px;
    margin: 0;
    font-style: normal;
    font-size: 12.5px;
    line-height: 16px;
  }
</style>
</head>
<body>
<main class="canvas">
  <section class="card card--front" aria-label="Business card front">
    <svg class="accent-panel" viewBox="0 0 442 264" aria-hidden="true">
      <polygon points="270,0 442,0 442,264 355,264" fill="var(--brand-purple)"/>
    </svg>
    <h1 class="wordmark"><span>Halvorsen</span><span>Electrical</span></h1>
    <div class="person">
      <p class="person__name">Marcus Ellery</p>
      <p class="person__role">Managing Director</p>
    </div>
    <ul class="contact">
      <li>
        <svg viewBox="0 0 10 10" aria-hidden="true"><path d="M1 3.5C1 2 2.5 1.5 5 1.5S9 2 9 3.5L7.5 4 7 3H3L2.5 4Z"/><rect x="2" y="4.5" width="6" height="4" rx="0.5"/></svg>
        044-987 654 321
      </li>
      <li>
        <svg viewBox="0 0 10 10" aria-hidden="true"><path d="M1 2.5h8v5H1z"/><path d="M1 2.5l4 3 4-3" stroke="#3a3a3a" stroke-width="0.8" fill="none"/></svg>
        hello@halvorsen.co
      </li>
    </ul>
    <address class="address">58, Foundry Lane,<br>Country Name, 30817</address>
  </section>

  <section class="card card--back" aria-label="Business card back">
    <h2 class="wordmark"><span>Halvorsen</span><span>Electrical</span></h2>
  </section>
</main>
</body>
</html>
```